Ember Lane Pet Supply

Thank you for your interest in this design contest. We are always welcome to questions and are looking forward to seeing what you can come up with.

We work on a Bootstrap platform with our custom built CMS. We require all designs to be sized accordingly with the bootstrap grid system found here: http://tilebasekit.com/css/#grid

At the start of a competition, we are looking for general Home Page Design concepts and an example product grid page.

Homepage: Slide Show/Featured Products/Specials

example website as a reference:https://www.brindlemoorgoods.com/

Store Product Grid: Show a grid of product thumbnails. Included elements are thumbnail and price. Also included are filters (sort by, show by grid/list).

No photos at this time but Logo is attached. Looking for good quality photo's around the web. Please read the attached creative brief in depth to get an idea f what the client is looking for. Thanks!

```html
<!DOCTYPE html>
<html lang="en">
<head>
<meta charset="utf-8">
<title>Ember Lane Pet Supply – Product Listing</title>
<link href="https://fonts.googleapis.com/css2?family=Open+Sans:wght@400;600;700&display=swap" rel="stylesheet">
<style>
:root{
  --green:#6aa823;
  --green-soft:#b6cc7b;
  --blue:#4aaccd;
  --brown:#5d4a33;
  --brown-bar:#6c5841;
  --beige:#e0d6b7;
  --beige-top:#e2d9bd;
  --page:#ececea;
  --ink:#555;
  --muted:#8b8b80;
  --orange:#e8821f;
  --white:#fff;
  --page-btn:#cbc3ab;
}
*{box-sizing:border-box;margin:0;padding:0}
html,body{width:837px;height:1200px;overflow:hidden}
body{font-family:"Open Sans",sans-serif;background:var(--page);position:relative;color:var(--ink)}
.abs{position:absolute}
/* top bar */
.topbar{left:0;top:0;width:837px;height:22px;background:var(--beige-top)}
.topbar nav{position:absolute;right:112px;top:6px;display:flex;gap:0;font-size:7px;color:#7b6d55}
.topbar nav span{padding:0 8px;border-left:1px solid #c7bb9b}
.topbar nav span:last-child{border-left:none}
/* header */
.header{left:0;top:22px;width:837px;height:68px;background:var(--white)}
.brand{position:absolute;left:114px;top:14px;display:flex;align-items:center;gap:6px}
.brand-dot{width:22px;height:22px;border-radius:50%;background:var(--brown)}
.brand-name{font-weight:700;font-size:12px;line-height:13px;color:var(--green);width:90px}
.mainnav{position:absolute;left:346px;top:24px;display:flex;gap:13px;font-size:7px;font-weight:700;color:#9a8f7a;letter-spacing:.2px}
.mainnav .active{color:var(--green);border-bottom:1px solid var(--green);padding-bottom:2px}
.search{position:absolute;left:565px;top:20px;width:91px;height:15px;border:1px solid #cfcfcf;font-size:6.5px;color:#aaa;padding:3px 5px}
.search svg{position:absolute;right:4px;top:3px}
.cart{position:absolute;left:668px;top:19px;display:flex;align-items:center;gap:7px;font-size:7px;font-weight:700;color:#9a8f7a}
.cart-ico{width:18px;height:18px;border-radius:50%;background:var(--green);display:flex;align-items:center;justify-content:center}
/* toolbar */
.page-title{left:113px;top:109px;font-size:13px;font-weight:700;color:var(--brown)}
.crumbs{left:222px;top:114px;font-size:7px;color:#7b6d55}
.crumbs b{font-weight:700}
.display{left:532px;top:113px;font-size:7.5px;font-weight:600;color:#444}
.view-list{left:568px;top:112px}
.view-grid{left:590px;top:112px}
.sort{left:610px;top:109px;width:115px;height:19px;background:var(--white);border:1px solid #ddd;font-size:7px;color:#999;padding:5px 8px}
.sort .caret{position:absolute;right:1px;top:1px;width:15px;height:15px;background:var(--green);display:flex;align-items:center;justify-content:center}
.sort-menu{left:610px;top:128px;width:115px;background:var(--white);border:1px solid #e3e3e3;z-index:5}
.sort-menu li{list-style:none;font-size:7px;color:#999;padding:6px 15px 7px;border-bottom:1px solid #eee}
.sort-menu li.on{color:var(--green);font-weight:700}
.sort-menu li:last-child{border-bottom:none}
/* product grid */
.grid{left:114px;top:150px;display:grid;grid-template-columns:repeat(3,192px);grid-auto-rows:225px;column-gap:17px;row-gap:23px}
.card{position:relative;background:var(--white);box-shadow:0 0 1px rgba(0,0,0,.12)}
.card .photo{position:absolute;left:9px;top:8px;width:173px;height:161px}
.photo.bed{background:linear-gradient(180deg,#f5c363 0%,#e8b060 45%,#c98a3f 58%,#1e3f7a 72%,#122a58 100%)}
.photo.lab{background:radial-gradient(ellipse at 55% 50%,#f4ecd9 0%,#e6dcc2 40%,#b9bd98 100%)}
.photo.yorkie{background:radial-gradient(ellipse at 50% 55%,#a9632f 0%,#c58a55 45%,#eac19a 100%)}
.card .name{position:absolute;left:10px;top:177px;font-size:10px;color:#444}
.card .price{position:absolute;left:10px;top:189px;font-size:12px;font-weight:700;color:var(--green)}
.card .buy{position:absolute;left:151px;top:176px;width:34px;height:34px;border-radius:50%;background:var(--green);display:flex;align-items:center;justify-content:center}
.ribbon{position:absolute;top:0}
.ribbon.new{right:-2px}
.ribbon.sale{left:-2px}
/* pagination */
.pager{left:578px;top:899px;display:flex;gap:5px}
.pager span{width:21px;height:21px;background:var(--page-btn);color:var(--white);font-size:8px;font-weight:700;display:flex;align-items:center;justify-content:center}
.pager span.cur{background:var(--brown-bar)}
.pager .gap{margin-left:15px}
.pager .gap2{margin-left:16px}
/* subscribe */
.subscribe{left:0;top:947px;width:837px;height:45px;background:var(--green-soft)}
.sub-brand{position:absolute;left:116px;top:12px;display:flex;align-items:center;gap:5px}
.sub-brand .brand-dot{width:16px;height:16px}
.sub-brand .brand-name{font-size:8px;line-height:9px;width:62px}
.sub-text{position:absolute;left:218px;top:15px;font-size:9.5px;font-weight:700;color:var(--white)}
.sub-input{position:absolute;left:426px;top:10px;width:185px;height:26px;background:var(--white);font-size:7px;color:#999;padding:9px 10px}
.sub-input svg{position:absolute;right:12px;top:9px}
.sub-btn{position:absolute;left:622px;top:9px;width:103px;height:27px;background:var(--orange);color:var(--white);font-size:7px;font-weight:700;display:flex;align-items:center;justify-content:center}
/* footer */
.footer{left:0;top:992px;width:837px;height:174px;background:var(--beige)}
.col{position:absolute;top:24px}
.col h4{font-size:10px;font-weight:600;color:var(--muted);margin-bottom:9px}
.col p,.col li{font-size:6.5px;color:#6e6450;line-height:12.5px;list-style:none}
.fb-count{color:var(--white)!important;font-size:6.5px}
.fb-like{width:23px;height:9px;background:var(--white);border:1px solid #bdb4a0;margin:3px 0 5px}
.avatars{display:grid;grid-template-columns:repeat(4,26px);gap:5px}
.avatars div{height:26px;background:linear-gradient(135deg,#8c7a66,#4d4438)}
.tweet{display:flex;gap:9px;margin-bottom:10px}
.tweet .dot{flex:none;width:22px;height:22px;border-radius:50%;background:var(--white);display:flex;align-items:center;justify-content:center}
.tweet p{width:95px;line-height:10px}
.info li{padding-left:10px;position:relative}
.info li::before{content:"›";position:absolute;left:0;color:#b3a888}
.social{display:flex;gap:7px;margin-top:16px}
.social span{width:18px;height:18px;border-radius:50%;background:var(--white);border:1px solid #d2c8aa}
/* bottom bar */
.bottombar{left:0;top:1166px;width:837px;height:34px;background:var(--brown-bar);color:var(--white);font-size:6.5px}
.bottombar .copy{position:absolute;left:113px;top:13px}
.bottombar nav{position:absolute;left:490px;top:13px;display:flex}
.bottombar nav span{padding:0 8px;border-left:1px solid #8c7a62}
.bottombar nav span:first-child{padding-left:0;border-left:none}
</style>
</head>
<body>

<div class="abs topbar">
  <nav><span>Account</span><span>Wishlist</span><span>Checkout</span><span>Log In</span><span>Sign Up</span></nav>
</div>

<header class="abs header">
  <div class="brand"><span class="brand-dot"></span><span class="brand-name">Ember Lane Pet Supply</span></div>
  <nav class="mainnav"><span class="active">HOME</span><span>DOG BEDS</span><span>COLLARS</span><span>LEASHES</span><span>CONTACT</span></nav>
  <div class="search">Search..
    <svg width="8" height="8" viewBox="0 0 8 8"><circle cx="3.2" cy="3.2" r="2.4" fill="none" stroke="#444" stroke-width="1.1"/><line x1="5" y1="5" x2="7.5" y2="7.5" stroke="#444" stroke-width="1.2"/></svg>
  </div>
  <div class="cart"><span class="cart-ico"><svg width="10" height="9" viewBox="0 0 10 9"><path d="M0 1h2l1.3 4.5h5L10 2H2.6" fill="none" stroke="#fff" stroke-width="1.1"/><circle cx="4" cy="7.6" r=".9" fill="#fff"/><circle cx="7.6" cy="7.6" r=".9" fill="#fff"/></svg></span>CART (0)</div>
</header>

<h1 class="abs page-title">Product Listing</h1>
<div class="abs crumbs">Home / Products / <b>Link</b></div>
<div class="abs display">Display:</div>
<svg class="abs view-list" width="13" height="11" viewBox="0 0 13 11"><g fill="#9a9a9a"><rect x="0" y="0" width="2" height="2"/><rect x="3" y="0" width="10" height="2"/><rect x="0" y="4.5" width="2" height="2"/><rect x="3" y="4.5" width="10" height="2"/><rect x="0" y="9" width="2" height="2"/><rect x="3" y="9" width="10" height="2"/></g></svg>
<svg class="abs view-grid" width="11" height="11" viewBox="0 0 11 11"><g fill="var(--green)"><rect x="0" y="0" width="3" height="3"/><rect x="4" y="0" width="3" height="3"/><rect x="8" y="0" width="3" height="3"/><rect x="0" y="4" width="3" height="3"/><rect x="4" y="4" width="3" height="3"/><rect x="8" y="4" width="3" height="3"/><rect x="0" y="8" width="3" height="3"/><rect x="4" y="8" width="3" height="3"/><rect x="8" y="8" width="3" height="3"/></g></svg>
<div class="abs sort">Newest
  <span class="caret"><svg width="7" height="5" viewBox="0 0 7 5"><path d="M.5 .8 3.5 4 6.5 .8" fill="none" stroke="#fff" stroke-width="1.2"/></svg></span>
</div>
<ul class="abs sort-menu">
  <li>Popular</li>
  <li class="on">Price High to Low</li>
  <li>Price Low to High</li>
  <li>Sale</li>
</ul>

<main class="abs grid">
  <!-- row 1 -->
  <div class="card"><div class="photo bed" role="img" aria-label="Golden retriever resting on a blue dog bed"></div>
    <svg class="ribbon new" width="66" height="66" viewBox="0 0 66 66"><polygon points="18,0 42,0 66,24 66,48" fill="var(--blue)"/><text x="44" y="24" transform="rotate(45 44 24)" font-family="Open Sans,sans-serif" font-size="9" font-weight="600" fill="#fff" text-anchor="middle" dominant-baseline="middle">NEW</text></svg>
    <div class="name">Blue Dog Bed</div><div class="price">$388.00</div>
    <div class="buy"><svg width="16" height="14" viewBox="0 0 16 14"><path d="M0 5h16M2 5l1.5 8h9L14 5M5 5l3-4 3 4M6 7v4M8 7v4M10 7v4" fill="none" stroke="#fff" stroke-width="1.4"/></svg></div></div>
  <div class="card"><div class="photo lab" role="img" aria-label="Labrador puppy chewing a red leash"></div>
    <div class="name">Blue Dog Bed</div><div class="price">$388.00</div>
    <div class="buy"><svg width="16" height="14" viewBox="0 0 16 14"><path d="M0 5h16M2 5l1.5 8h9L14 5M5 5l3-4 3 4M6 7v4M8 7v4M10 7v4" fill="none" stroke="#fff" stroke-width="1.4"/></svg></div></div>
  <div class="card"><div class="photo yorkie" role="img" aria-label="Yorkshire terrier wearing a collar"></div>
    <svg class="ribbon sale" width="66" height="66" viewBox="0 0 66 66"><polygon points="24,0 48,0 0,48 0,24" fill="var(--green)"/><text x="22" y="22" transform="rotate(-45 22 22)" font-family="Open Sans,sans-serif" font-size="9" font-weight="600" fill="#fff" text-anchor="middle" dominant-baseline="middle">SALE</text></svg>
    <div class="name">Blue Dog Bed</div><div class="price">$388.00</div>
    <div class="buy"><svg width="16" height="14" viewBox="0 0 16 14"><path d="M0 5h16M2 5l1.5 8h9L14 5M5 5l3-4 3 4M6 7v4M8 7v4M10 7v4" fill="none" stroke="#fff" stroke-width="1.4"/></svg></div></div>
  <!-- row 2 -->
  <div class="card"><div class="photo bed" role="img" aria-label="Golden retriever resting on a blue dog bed"></div>
    <svg class="ribbon new" width="66" height="66" viewBox="0 0 66 66"><polygon points="18,0 42,0 66,24 66,48" fill="var(--blue)"/><text x="44" y="24" transform="rotate(45 44 24)" font-family="Open Sans,sans-serif" font-size="9" font-weight="600" fill="#fff" text-anchor="middle" dominant-baseline="middle">NEW</text></svg>
    <div class="name">Blue Dog Bed</div><div class="price">$388.00</div>
    <div class="buy"><svg width="16" height="14" viewBox="0 0 16 14"><path d="M0 5h16M2 5l1.5 8h9L14 5M5 5l3-4 3 4M6 7v4M8 7v4M10 7v4" fill="none" stroke="#fff" stroke-width="1.4"/></svg></div></div>
  <div class="card"><div class="photo lab" role="img" aria-label="Labrador puppy chewing a red leash"></div>
    <div class="name">Blue Dog Bed</div><div class="price">$388.00</div>
    <div class="buy"><svg width="16" height="14" viewBox="0 0 16 14"><path d="M0 5h16M2 5l1.5 8h9L14 5M5 5l3-4 3 4M6 7v4M8 7v4M10 7v4" fill="none" stroke="#fff" stroke-width="1.4"/></svg></div></div>
  <div class="card"><div class="photo yorkie" role="img" aria-label="Yorkshire terrier wearing a collar"></div>
    <svg class="ribbon sale" width="66" height="66" viewBox="0 0 66 66"><polygon points="24,0 48,0 0,48 0,24" fill="var(--green)"/><text x="22" y="22" transform="rotate(-45 22 22)" font-family="Open Sans,sans-serif" font-size="9" font-weight="600" fill="#fff" text-anchor="middle" dominant-baseline="middle">SALE</text></svg>
    <div class="name">Blue Dog Bed</div><div class="price">$388.00</div>
    <div class="buy"><svg width="16" height="14" viewBox="0 0 16 14"><path d="M0 5h16M2 5l1.5 8h9L14 5M5 5l3-4 3 4M6 7v4M8 7v4M10 7v4" fill="none" stroke="#fff" stroke-width="1.4"/></svg></div></div>
  <!-- row 3 -->
  <div class="card"><div class="photo bed" role="img" aria-label="Golden retriever resting on a blue dog bed"></div>
    <svg class="ribbon new" width="66" height="66" viewBox="0 0 66 66"><polygon points="18,0 42,0 66,24 66,48" fill="var(--blue)"/><text x="44" y="24" transform="rotate(45 44 24)" font-family="Open Sans,sans-serif" font-size="9" font-weight="600" fill="#fff" text-anchor="middle" dominant-baseline="middle">NEW</text></svg>
    <div class="name">Blue Dog Bed</div><div class="price">$388.00</div>
    <div class="buy"><svg width="16" height="14" viewBox="0 0 16 14"><path d="M0 5h16M2 5l1.5 8h9L14 5M5 5l3-4 3 4M6 7v4M8 7v4M10 7v4" fill="none" stroke="#fff" stroke-width="1.4"/></svg></div></div>
  <div class="card"><div class="photo lab" role="img" aria-label="Labrador puppy chewing a red leash"></div>
    <div class="name">Blue Dog Bed</div><div class="price">$388.00</div>
    <div class="buy"><svg width="16" height="14" viewBox="0 0 16 14"><path d="M0 5h16M2 5l1.5 8h9L14 5M5 5l3-4 3 4M6 7v4M8 7v4M10 7v4" fill="none" stroke="#fff" stroke-width="1.4"/></svg></div></div>
  <div class="card"><div class="photo yorkie" role="img" aria-label="Yorkshire terrier wearing a collar"></div>
    <svg class="ribbon sale" width="66" height="66" viewBox="0 0 66 66"><polygon points="24,0 48,0 0,48 0,24" fill="var(--green)"/><text x="22" y="22" transform="rotate(-45 22 22)" font-family="Open Sans,sans-serif" font-size="9" font-weight="600" fill="#fff" text-anchor="middle" dominant-baseline="middle">SALE</text></svg>
    <div class="name">Blue Dog Bed</div><div class="price">$388.00</div>
    <div class="buy"><svg width="16" height="14" viewBox="0 0 16 14"><path d="M0 5h16M2 5l1.5 8h9L14 5M5 5l3-4 3 4M6 7v4M8 7v4M10 7v4" fill="none" stroke="#fff" stroke-width="1.4"/></svg></div></div>
</main>

<nav class="abs pager">
  <span><svg width="6" height="8" viewBox="0 0 6 8"><path d="M5 .5 1.5 4 5 7.5" fill="none" stroke="#fff" stroke-width="1.5"/></svg></span>
  <span class="cur gap">1</span><span>2</span><span>3</span>
  <span class="gap2"><svg width="6" height="8" viewBox="0 0 6 8"><path d="M1 .5 4.5 4 1 7.5" fill="none" stroke="#fff" stroke-width="1.5"/></svg></span>
</nav>

<section class="abs subscribe">
  <div class="sub-brand"><span class="brand-dot"></span><span class="brand-name">Ember Lane Pet Supply</span></div>
  <div class="sub-text">Sign up and get the latest product updates</div>
  <div class="sub-input">Enter Your Email *
    <svg width="10" height="7" viewBox="0 0 10 7"><rect x=".5" y=".5" width="9" height="6" fill="none" stroke="#e8821f"/><path d="M.5 .5 5 4 9.5 .5" fill="none" stroke="#e8821f"/></svg>
  </div>
  <div class="sub-btn">SUBSCRIBE NOW</div>
</section>

<footer class="abs footer">
  <div class="col" style="left:113px">
    <h4>Pawcircle</h4>
    <p class="fb-count">20000 Members</p>
    <div class="fb-like"></div>
    <div class="avatars" role="img" aria-label="Member profile pictures">
      <div></div><div></div><div></div><div></div><div></div><div></div><div></div><div></div>
    </div>
    <p style="margin-top:6px">Pawcircle social plugin</p>
  </div>
  <div class="col" style="left:271px">
    <h4>From Chirpline</h4>
    <div class="tweet"><span class="dot"><svg width="9" height="9" viewBox="0 0 9 9"><circle cx="4.5" cy="4.5" r="3" fill="#555"/></svg></span><p>Lorem Ipsum is simply dummy text of the printing and typesetting industry. <b>#Lorem Ipsum @industrys</b></p></div>
    <div class="tweet"><span class="dot"><svg width="9" height="9" viewBox="0 0 9 9"><circle cx="4.5" cy="4.5" r="3" fill="#555"/></svg></span><p>Lorem Ipsum is simply dummy text of the printing and typesetting industry. <b>#Lorem Ipsum @industrys</b></p></div>
  </div>
  <div class="col info" style="left:426px">
    <h4>Information</h4>
    <ul>
      <li>Sed ultrices purus non.</li>
      <li>sodales sodales.</li>
      <li>Curabitur pretium dui vitae.</li>
      <li>Donec gravida mi in nisl</li>
      <li>faucibus leo condimentum.</li>
      <li>Donec et lorem suscipit.</li>
    </ul>
  </div>
  <div class="col" style="left:585px">
    <h4>Contact Us</h4>
    <p>Ember Lane Supply</p>
    <p>Your Street, Your Town</p>
    <p>Your Country</p>
    <p>+1 555-0142-7731</p>
    <p>hello@emberlanepets.com</p>
    <div class="social"><span></span><span></span><span></span><span></span></div>
  </div>
</footer>

<div class="abs bottombar">
  <div class="copy">© Copyright 2014. Ember Lane Pet Supply , All Rights Reserved.</div>
  <nav><span>About Us</span><span>Delivery &amp; Returns</span><span>Terms &amp; Conditions</span><span>Contact Us</span></nav>
</div>

</body>
</html>
```